Brightloom Reach - Business Card

We need a business card for a Social Media Marketing company that specializes in online marketing for small businesses in Canada using common Social Media platforms such as Instagram, Facebook, Snapchat & Twitter.

I have uploaded a copy of our logo which I would like utilized in the business card. We would like the business card to be modern yet classy design.

Our website is www.brightloomreach.ca

Industry/Entity Type

Marketing

Contact Information for Business Card

Email: info@brightloomreach.ca
Website: www.brightloomreach.ca
Telephone: 604-352-9081

Colors

Designer to choose colors to be used in the design.

Requirements
Must have
• Social Media icons on reverse
• Please add some designs with color.

```html
<!DOCTYPE html>
<html lang="en">
<head>
<meta charset="utf-8">
<title>Brightloom Reach - Business Card</title>
<link rel="stylesheet" href="https://fonts.googleapis.com/css2?family=Roboto:wght@400;500&family=Roboto+Condensed:wght@400;700&display=swap">
<style>
  :root {
    --backdrop: #e6e6e6;
    --card-light: #f4f4f4;
    --card-dark: #3a3e41;
    --ink: #3a3e41;
    --ink-soft: #a9abad;
    --band-light: #b3b5b7;
    --white: #ffffff;
  }
  * { margin: 0; padding: 0; box-sizing: border-box; }
  html, body { width: 1200px; height: 960px; overflow: hidden; }
  body {
    background: var(--backdrop);
    position: relative;
    font-family: "Roboto", Arial, sans-serif;
  }
  .card {
    position: absolute;
    width: 601px;
    height: 343px;
    box-shadow: 0 2px 5px rgba(0,0,0,0.25);
  }
  .card--front { left: 314px; top: 113px; background: var(--card-light); overflow: hidden; }
  .card--back { left: 311px; top: 472px; background: var(--card-dark); }

  .front-band { position: absolute; left: 0; bottom: 0; width: 601px; height: 19px; }

  .brand {
    position: absolute;
    display: flex;
    flex-direction: column;
    align-items: center;
    font-family: "Roboto Condensed", Arial, sans-serif;
    font-weight: 700;
    line-height: 1;
    text-transform: uppercase;
    text-align: center;
  }
  .brand__name { font-size: 29px; letter-spacing: 0.5px; }
  .brand__mark { width: 12px; height: 12px; margin-top: 14px; }
  .card--front .brand { left: 93px; top: 137px; width: 150px; color: var(--ink); }
  .card--front .brand__mark { background: var(--ink); }
  .card--back .brand { left: 200px; top: 120px; width: 200px; color: var(--white); }
  .card--back .brand__name { font-size: 34px; }
  .card--back .brand__mark { background: var(--white); }

  .divider {
    position: absolute;
    left: 306px; top: 97px;
    width: 1px; height: 145px;
    background: #c9c9c9;
  }

  .person { position: absolute; left: 343px; top: 112px; }
  .person__name {
    font-family: "Roboto Condensed", Arial, sans-serif;
    font-weight: 700;
    font-size: 21px;
    color: var(--ink);
    letter-spacing: 0.3px;
  }
  .person__role {
    font-family: "Roboto Condensed", Arial, sans-serif;
    font-size: 14px;
    color: var(--ink-soft);
    margin-top: 2px;
  }
  .contact { position: absolute; left: 343px; top: 176px; list-style: none; }
  .contact__item {
    display: flex; align-items: center;
    height: 19.5px;
    font-size: 14px;
    color: var(--ink);
  }
  .contact__icon { width: 12px; height: 12px; margin-right: 10px; fill: var(--ink); }

  .social {
    position: absolute;
    left: 119px; top: 283px;
    width: 362px; height: 28px;
    display: flex; align-items: center; justify-content: center;
  }
  .social__rule { height: 1px; width: 125px; }
  .social__rule--left { background: linear-gradient(to right, transparent, #cfd1d2); margin-right: 6px; }
  .social__rule--right { background: linear-gradient(to left, transparent, #cfd1d2); margin-left: 6px; }
  .social__dot {
    width: 27px; height: 27px;
    border: 1.5px solid var(--white);
    border-radius: 50%;
    margin: 0 3.5px;
  }
</style>
</head>
<body>
  <section class="card card--front" aria-label="Front of card">
    <div class="brand">
      <span class="brand__name">Brightloom<br>Reach</span>
      <span class="brand__mark"></span>
    </div>
    <div class="divider"></div>
    <div class="person">
      <p class="person__name">MAREN HOLT</p>
      <p class="person__role">CEO/FOUNDER</p>
    </div>
    <ul class="contact">
      <li class="contact__item">
        <svg class="contact__icon" viewBox="0 0 12 12"><path d="M2.5 0.5 L4.3 0.5 L5 3.2 L3.8 4.2 C4.5 5.7 6.3 7.5 7.8 8.2 L8.8 7 L11.5 7.7 L11.5 9.5 C11.5 10.6 10.6 11.5 9.5 11.5 C4.5 11.2 0.8 7.5 0.5 2.5 C0.5 1.4 1.4 0.5 2.5 0.5 Z"/></svg>
        604-352-9081
      </li>
      <li class="contact__item">
        <svg class="contact__icon" viewBox="0 0 12 12"><path d="M0.5 2 H11.5 V3 L6 6.5 L0.5 3 Z M0.5 4.3 L6 7.8 L11.5 4.3 V10 H0.5 Z"/></svg>
        info@brightloomreach.ca
      </li>
      <li class="contact__item">
        <svg class="contact__icon" viewBox="0 0 12 12"><circle cx="6" cy="6" r="5.5"/><path d="M3 3.5 C4.5 3 5 4.5 4 5.5 C3.5 6.5 5 7.5 4.5 9" stroke="#f4f4f4" stroke-width="1.2" fill="none"/><path d="M8 2.5 C7 4 9 5 8.5 6.5" stroke="#f4f4f4" stroke-width="1.2" fill="none"/></svg>
        www.brightloomreach.ca
      </li>
    </ul>
    <svg class="front-band" viewBox="0 0 601 19" preserveAspectRatio="none">
      <polygon points="0,0 391,0 386,19 0,19" fill="var(--card-dark)"/>
      <polygon points="394,0 601,0 601,19 389,19" fill="var(--band-light)"/>
    </svg>
  </section>

  <section class="card card--back" aria-label="Back of card">
    <div class="brand">
      <span class="brand__name">Brightloom<br>Reach</span>
      <span class="brand__mark"></span>
    </div>
    <div class="social" aria-label="Social media links">
      <span class="social__rule social__rule--left"></span>
      <span class="social__dot"></span>
      <span class="social__dot"></span>
      <span class="social__dot"></span>
      <span class="social__rule social__rule--right"></span>
    </div>
  </section>
</body>
</html>
```